1923 Basins & Spouts Business Card

I'm wanting to get a business card designed. Our business is 1923 Basins & Spouts
Details for the card:

1923 Basins & Spouts
Name: Gareth Vostle
Email: gareth@1923basinsandspouts.com.au
Website: www.1923basinsandspouts.com.au
Mobile: 0439 602 158
Phone: 02 5550 1843

Font of Basins & Spouts is called Snell Roundhand. Not sue what font logo text is.

I'm thinking two sided but it doesn't have to be.

```html
<!DOCTYPE html>
<html lang="en">
<head>
<meta charset="utf-8">
<title>1923 Basins &amp; Spouts – Business Card</title>
<link rel="stylesheet" href="https://fonts.googleapis.com/css2?family=Lato:wght@400;700&family=Mulish:wght@700&display=swap">
<style>
  :root {
    --backdrop: #8a8a8a;
    --card-white: #ffffff;
    --card-black: #0a0a0b;
    --ink: #111111;
    --contact-grey: #555555;
    --swoosh-grey: #6b6b6b;
    --on-dark: #ffffff;
  }
  html, body {
    margin: 0;
    padding: 0;
    width: 1200px;
    height: 1200px;
    overflow: hidden;
    background: var(--backdrop);
  }
  .canvas {
    position: relative;
    width: 1200px;
    height: 1200px;
  }
  .card {
    position: absolute;
    left: 240px;
    width: 720px;
    height: 420px;
    border-radius: 29px;
    overflow: hidden;
  }
  .card--front { top: 142px; background: var(--card-white); }
  .card--back { top: 638px; background: var(--card-black); }

  .front__accent {
    position: absolute;
    left: 0; top: 151px;
    width: 8px; height: 29px;
    background: var(--ink);
  }
  .front__name {
    position: absolute;
    left: 35px; top: 150px;
    margin: 0;
    font-family: "Mulish", sans-serif;
    font-weight: 700;
    font-size: 26px;
    line-height: 28px;
    color: var(--ink);
  }
  .contact-list {
    position: absolute;
    left: 34px; top: 231px;
    margin: 0; padding: 0;
    list-style: none;
    font-family: "Lato", sans-serif;
    font-size: 18px;
    color: var(--contact-grey);
  }
  .contact-list li {
    display: flex;
    align-items: center;
    height: 26px;
  }
  .contact-list svg {
    width: 13px; height: 13px;
    margin-right: 12px;
    fill: var(--ink);
  }
  .front__brand {
    position: absolute;
    left: 440px; top: 70px;
    width: 240px; height: 166px;
    display: flex;
    align-items: center;
    justify-content: center;
    text-align: center;
    font-family: "Lato", sans-serif;
    font-weight: 700;
    font-size: 30px;
    line-height: 1.25;
    color: var(--ink);
  }
  .front__swoosh {
    position: absolute;
    left: 0; top: 0;
    width: 720px; height: 420px;
  }
  .swoosh-band { fill: var(--card-black); }
  .swoosh-line { fill: var(--swoosh-grey); }
  .front__address {
    position: absolute;
    right: 30px; top: 352px;
    margin: 0;
    text-align: right;
    font-family: "Lato", sans-serif;
    font-style: normal;
    font-size: 16px;
    line-height: 20px;
    color: var(--on-dark);
  }

  .back__lockup {
    position: absolute;
    left: 0; top: 188px;
    width: 720px;
    text-align: center;
    color: var(--on-dark);
    font-family: "Lato", sans-serif;
  }
  .back__brand {
    margin: 0;
    font-weight: 700;
    font-size: 38px;
    line-height: 46px;
  }
  .back__tagline {
    margin: 10px 0 0;
    font-weight: 400;
    font-size: 14px;
    line-height: 18px;
    letter-spacing: 0.2px;
  }
  .back__footer {
    position: absolute;
    left: 0; top: 360px;
    width: 720px;
    margin: 0;
    text-align: center;
    font-family: "Lato", sans-serif;
    font-size: 18px;
    line-height: 22px;
    color: var(--on-dark);
  }
</style>
</head>
<body>
<main class="canvas">

  <section class="card card--front" aria-label="Card front">
    <span class="front__accent"></span>
    <h1 class="front__name">Gareth Vostle</h1>

    <ul class="contact-list">
      <li>
        <svg viewBox="0 0 16 16" aria-hidden="true"><path d="M3.5 1.5l2.5 0 1 3.5-1.7 1.2a8 8 0 0 0 4.5 4.5L11 9l3.5 1v2.5c0 1-1 2-2 2C6.5 14.5 1.5 9.5 1.5 3.5c0-1 1-2 2-2z"/></svg>
        02 5550 1843
      </li>
      <li>
        <svg viewBox="0 0 16 16" aria-hidden="true"><path d="M4.5 0.5h7a1 1 0 0 1 1 1v13a1 1 0 0 1-1 1h-7a1 1 0 0 1-1-1v-13a1 1 0 0 1 1-1zM5 2.5v9.5h6V2.5zM8 12.8a0.9 0.9 0 1 0 0.01 0z"/></svg>
        0439 602 158
      </li>
      <li>
        <svg viewBox="0 0 16 16" aria-hidden="true"><path d="M1 3h14v10H1zM2.5 4.5v0.6L8 9l5.5-3.9V4.5z"/></svg>
        gareth@1923basinsandspouts.com.au
      </li>
      <li>
        <svg viewBox="0 0 16 16" aria-hidden="true"><path d="M8 1a7 7 0 1 0 0.01 0zM5 4.5l3 1 1 2.5-2 1.5 0.5 3-2-1.5-0.5-3-2-1zM11 3.5l1.5 2-1 2.5-1.5-1z"/></svg>
        www.1923basinsandspouts.com.au
      </li>
    </ul>

    <div class="front__brand">1923 Basins &amp; Spouts</div>

    <svg class="front__swoosh" viewBox="0 0 720 420" aria-hidden="true">
      <path class="swoosh-line" d="M0 366 Q330 350 622 318 Q340 362 0 382 Z"/>
      <path class="swoosh-band" d="M0 388 Q380 366 720 300 L720 420 L0 420 Z"/>
    </svg>

    <address class="front__address">
      Tallis Crossing<br>
      Marrowgate Kempley, 1627
    </address>
  </section>

  <section class="card card--back" aria-label="Card back">
    <div class="back__lockup">
      <p class="back__brand">1923 Basins &amp; Spouts</p>
      <p class="back__tagline">Enduring elegance meets effortless everyday function</p>
    </div>
    <p class="back__footer">1923 Basins &amp; Spouts</p>
  </section>

</main>
</body>
</html>
```